Etiketten-Design für Produkte eines Familienbetriebs mit Imkerei und Hühnerhaltung
Zielgruppe
Wir sind ein Familienbetrieb mit Imkerei und Hühnerhaltung. Wir suchen für unsere Produkte ein modernes Corporate Design, mit zentralen, bei jedem Produkt vorkommenden Elementen, sowie Elementen, welche produktindividuell sind.
Wir leben in einem 150 jährigen Riegelhaus, welches in der Umgebung sehr bekannt ist. Es soll im Etiketten-Design zentral erscheinen.
Unsere Produkte sind: Honig, Pollen, Eier
Aufgabenstellung
1. Zentrale, auf allen Etiketten wiederkehrende Elemente:
- Unser Riegelhaus (stilisiert) (Bild beiliegend)
- Das Wort 'Birkeneck' (Anmerkung: ohne Anführungszeichen)
- die zentralen Elemente sollen die Produkte nicht überragen.
2. Dezente Adresse:
- Familie Dorbach, Birkeneck, CH-9573 Holtikon
3. Produkte:
a) Honig
Sorten: Waldhonig (dunkel), Blütenhonig (gelblich-goldig), Crèmehonig (gelblich-weisslich), Lavendelhonig (gelblich-goldig)
Die Honigsorten sollen farblich hervortreten.
Freifeld (zweizeilig): für die Lotnummer und die Haltbarkeitsangabe)
Gewicht: 250 g, 500 g
b) Pollen
Gewicht: 100 g
c) Eier
Verpackungseinheiten: 4er-, 6er-, 10er-Packung
Haltungsform: BIO-Haltung
das Wort 'frisch'
Farbe grün (=Bio) soll farblich hervortreten (ähnlich wie beim Honig)
Freifeld (zweizeilig: für das Eigewicht und die Haltbarkeitsangabe)
Bitte keine Stock-Bilder verwenden. Die Etiketten sollen schlicht, edel ,schörkellos und modern erscheinen.
Das Etikett soll Exklusivität und Qualität ausstrahlen. Etikettenhintergrund einfarbig.
Interessanterweise gibt es bei Weinen solche Etiketten. Ich habe einige rausgesucht und angehängt, um die Richtung vorzugeben. (Wein1-6)
Ich habe auch eine schlichte Honigetikette gefunden, die ins Schema passt. (Imker1)
Zusätzlich sind jetzt auch noch Farbbeispiele der Honigsorten zur besseren Abstimmung von Inhalt und Etikette beigelegt. Lavendelhonig ist dem Blütenhonig sehr ähnlich.
Etikettengrössen:
Honig/Pollen 250 g: 190 x 42 mm
Honig 500 g: 206 x 45 mm
Eier 4er: 60 x 60 mm
Eier 6er: 110 x 60 mm
Eier 10er: 170 x 60 cm

```html
<!DOCTYPE html>
<html lang="de">
<head>
<meta charset="utf-8">
<title>Birkeneck – Honig- und Pollenetiketten</title>
<link rel="stylesheet" href="https://fonts.googleapis.com/css2?family=Roboto+Condensed:wght@400;700&family=PT+Sans:wght@400;700&display=swap">
<style>
  :root{
    --cream:#fdf6cc;
    --white:#ffffff;
    --field:#ffffff;
    --creme:#7b4b22;
    --bluete:#d3a82b;
    --wald-dunkel:#3f4436;
    --wald-gruen:#4d9a67;
    --lavendel:#8b77a8;
    --pollen-1007:#e58b27;
    --pollen-1033:#f29a22;
    --pollen-2003:#ec7430;
    --ink:#2f2a22;
  }
  *{box-sizing:border-box}
  html,body{margin:0;padding:0;overflow:hidden}
  body{width:1200px;height:501px;background:var(--white);position:relative;font-family:"PT Sans",sans-serif}

  .sheet{position:absolute;inset:0}
  .column{position:absolute;top:0}
  .col-250{left:30px}
  .col-500{left:397px}
  .col-pollen{left:807px}

  .label{position:absolute;left:0;width:348px;height:77px;background:var(--cream);overflow:hidden;color:var(--c)}
  .col-500 .label{transform:scale(1.086);transform-origin:0 0}

  .creme{--c:var(--creme);--t:var(--ink)}
  .bluete{--c:var(--bluete);--t:var(--bluete)}
  .wald-dunkel{--c:var(--wald-dunkel);--t:var(--ink)}
  .wald-gruen{--c:var(--wald-gruen);--t:var(--wald-gruen)}
  .lavendel{--c:var(--lavendel);--t:var(--lavendel)}
  .pollen-1007{--c:var(--pollen-1007);--t:var(--pollen-1007)}
  .pollen-1033{--c:var(--pollen-1033);--t:var(--pollen-1033)}
  .pollen-2003{--c:var(--pollen-2003);--t:var(--pollen-2003)}

  .variety{position:absolute;left:0;top:0;width:93px;height:100%;background:var(--c);color:var(--white);text-align:center}
  .variety h2{margin:10px 0 0;font:700 9px/1 "Roboto Condensed",sans-serif;letter-spacing:.01em}
  .region{margin-top:3px;font-size:3.9px;letter-spacing:.14em;text-transform:uppercase;opacity:.8}
  .rule{width:17px;height:.6px;background:var(--white);margin:3.5px auto 4px}
  .story{margin:0 6px;font-size:3.6px;line-height:1.36}
  .pollen .story{font-size:3.05px;line-height:1.3;margin:0 5px}

  .comb{position:absolute;left:93px;top:0;width:36px;height:34px;background:linear-gradient(135deg,color-mix(in srgb,var(--c) 22%,transparent),transparent 75%)}
  .house{position:absolute;left:140px;top:8px;width:70px;height:36px;background:color-mix(in srgb,var(--c) 30%,var(--cream));border-radius:2px}
  .brand{position:absolute;left:108px;top:46px;width:120px;text-align:center;font:400 19px/1 "Roboto Condensed",sans-serif;color:var(--c)}

  .info{position:absolute;left:240px;top:8px;right:5px;color:var(--t)}
  .info h3{margin:0;font:700 8.5px/1 "Roboto Condensed",sans-serif;color:var(--c)}
  .field{display:flex;align-items:center;margin-top:6px;font-size:3.8px;line-height:1.15}
  .field span{width:25px}
  .field i{display:block;height:8px;width:64px;margin-left:15px;background:var(--field)}
  .field + .field{margin-top:8px}
  .weight{margin-top:7px;font-size:3.8px;letter-spacing:.12em}
  .weight b{font:700 7.5px/1 "Roboto Condensed",sans-serif;letter-spacing:0;margin-left:1px}
  .address{margin-top:3px;font-size:3.6px}

  .ral{position:absolute;left:1163px;font:400 6.8px/1 "PT Sans",sans-serif;color:var(--ink)}
</style>
</head>
<body>
<main class="sheet">

  <!-- 250 g -->
  <section class="column col-250">
    <article class="label creme" style="top:48px">
      <div class="variety"><h2>Crèmehonig</h2><div class="region">Natürliches aus dem Thurgau</div><div class="rule"></div>
        <p class="story">Unser Waldhonig ist Mischung aus Honigtau von verschiedenen Bäumen. Meistens enthält er auch Waldblütenhonig.Er ist zähflüssig und schmeckt würzig, kräftig, fast malzig. Die Farbe reicht von hellbraun über rotbraun bis dunkelbraun.</p></div>
      <div class="comb" role="img" aria-label="Wabenmuster"></div>
      <div class="house" role="img" aria-label="Stilisiertes Riegelhaus"></div>
      <div class="brand">Birkeneck</div>
      <div class="info"><h3>100% Schweizer Honig</h3>
        <div class="field"><span>Mindestens haltbar bis:</span><i></i></div>
        <div class="field"><span>Lot Nr.:</span><i></i></div>
        <div class="weight">Netto <b>250 g</b></div>
        <div class="address">Familie Dorbach, Birkeneck, CH-9573 Holtikon</div></div>
    </article>

    <article class="label bluete" style="top:136px">
      <div class="variety"><h2>Blütenhonig</h2><div class="region">Natürliches aus dem Thurgau</div><div class="rule"></div>
        <p class="story">Unser Waldhonig ist Mischung aus Honigtau von verschiedenen Bäumen. Meistens enthält er auch Waldblütenhonig.Er ist zähflüssig und schmeckt würzig, kräftig, fast malzig. Die Farbe reicht von hellbraun über rotbraun bis dunkelbraun.</p></div>
      <div class="comb" role="img" aria-label="Wabenmuster"></div>
      <div class="house" role="img" aria-label="Stilisiertes Riegelhaus mit Biene"></div>
      <div class="brand">Birkeneck</div>
      <div class="info"><h3>100% Schweizer Honig</h3>
        <div class="field"><span>Mindestens haltbar bis:</span><i></i></div>
        <div class="field"><span>Lot Nr.:</span><i></i></div>
        <div class="weight">Netto <b>250 g</b></div>
        <div class="address">Familie Dorbach, Birkeneck, CH-9573 Holtikon</div></div>
    </article>

    <article class="label wald-dunkel" style="top:227px">
      <div class="variety"><h2>Waldhonig</h2><div class="region">Natürliches aus dem Thurgau</div><div class="rule"></div>
        <p class="story">Honig ist ein Naturprodukt und sein Geschmack variiert je nach Nektarangebot von Jahr zu Jahr. Wir tragen Sorge zu unseren Bienen und bieten ihnen auf unserer Wiesenblumenwiese und den Obstanlagen vom Frühling bis in den Herbst ein vielfältiges Nahrungsangebot. Die reiche Vielfalt an Wiesenblumen gibt unserem Honig seinen milden und im Gaumen gehaltvollen Geschmack.</p></div>
      <div class="comb" role="img" aria-label="Wabenmuster"></div>
      <div class="house" role="img" aria-label="Stilisiertes Riegelhaus mit Biene"></div>
      <div class="brand">Birkeneck</div>
      <div class="info"><h3>100% Schweizer Honig</h3>
        <div class="field"><span>Mindestens haltbar bis:</span><i></i></div>
        <div class="field"><span>Lot Nr.:</span><i></i></div>
        <div class="weight">Netto <b>250 g</b></div>
        <div class="address">Familie Dorbach, Birkeneck, CH-9573 Holtikon</div></div>
    </article>

    <article class="label wald-gruen" style="top:308px">
      <div class="variety"><h2>Waldhonig</h2><div class="region">Natürliches aus dem Thurgau</div><div class="rule"></div>
        <p class="story">Honig ist ein Naturprodukt und sein Geschmack variiert je nach Nektarangebot von Jahr zu Jahr. Wir tragen Sorge zu unseren Bienen und bieten ihnen auf unserer Wiesenblumenwiese und den Obstanlagen vom Frühling bis in den Herbst ein vielfältiges Nahrungsangebot. Die reiche Vielfalt an Wiesenblumen gibt unserem Honig seinen milden und im Gaumen gehaltvollen Geschmack.</p></div>
      <div class="comb" role="img" aria-label="Wabenmuster"></div>
      <div class="house" role="img" aria-label="Stilisiertes Riegelhaus mit Biene"></div>
      <div class="brand">Birkeneck</div>
      <div class="info"><h3>100% Schweizer Honig</h3>
        <div class="field"><span>Mindestens haltbar bis:</span><i></i></div>
        <div class="field"><span>Lot Nr.:</span><i></i></div>
        <div class="weight">Netto <b>250 g</b></div>
        <div class="address">Familie Dorbach, Birkeneck, CH-9573 Holtikon</div></div>
    </article>

    <article class="label lavendel" style="top:397px">
      <div class="variety"><h2>Lavendelhonig</h2><div class="region">Natürliches aus dem Thurgau</div><div class="rule"></div>
        <p class="story">Diesen Lavendelhonig haben unsere Bienen auf unserem eigenen Lavendelfeld gesammelt. Wir ernten ihn nur einmal im Jahr, wenn der Lavendel in Vollblüte steht. Dieser rare Honig zeichnet sich durch seinen typischen Lavendelgeschmack aus.</p></div>
      <div class="comb" role="img" aria-label="Wabenmuster"></div>
      <div class="house" role="img" aria-label="Stilisiertes Riegelhaus mit Biene"></div>
      <div class="brand">Birkeneck</div>
      <div class="info"><h3>100% Schweizer Honig</h3>
        <div class="field"><span>Mindestens haltbar bis:</span><i></i></div>
        <div class="field"><span>Lot Nr.:</span><i></i></div>
        <div class="weight">Netto <b>250 g</b></div>
        <div class="address">Familie Dorbach, Birkeneck, CH-9573 Holtikon</div></div>
    </article>
  </section>

  <!-- 500 g -->
  <section class="column col-500">
    <article class="label creme" style="top:22px">
      <div class="variety"><h2>Crèmehonig</h2><div class="region">Natürliches aus dem Thurgau</div><div class="rule"></div>
        <p class="story">Unser Waldhonig ist Mischung aus Honigtau von verschiedenen Bäumen. Meistens enthält er auch Waldblütenhonig.Er ist zähflüssig und schmeckt würzig, kräftig, fast malzig. Die Farbe reicht von hellbraun über rotbraun bis dunkelbraun.</p></div>
      <div class="comb" role="img" aria-label="Wabenmuster"></div>
      <div class="house" role="img" aria-label="Stilisiertes Riegelhaus"></div>
      <div class="brand">Birkeneck</div>
      <div class="info"><h3>100% Schweizer Honig</h3>
        <div class="field"><span>Mindestens haltbar bis:</span><i></i></div>
        <div class="field"><span>Lot Nr.:</span><i></i></div>
        <div class="weight">Netto <b>500 g</b></div>
        <div class="address">Familie Dorbach, Birkeneck, CH-9573 Holtikon</div></div>
    </article>

    <article class="label bluete" style="top:115px">
      <div class="variety"><h2>Blütenhonig</h2><div class="region">Natürliches aus dem Thurgau</div><div class="rule"></div>
        <p class="story">Unser Waldhonig ist Mischung aus Honigtau von verschiedenen Bäumen. Meistens enthält er auch Waldblütenhonig.Er ist zähflüssig und schmeckt würzig, kräftig, fast malzig. Die Farbe reicht von hellbraun über rotbraun bis dunkelbraun.</p></div>
      <div class="comb" role="img" aria-label="Wabenmuster"></div>
      <div class="house" role="img" aria-label="Stilisiertes Riegelhaus mit Biene"></div>
      <div class="brand">Birkeneck</div>
      <div class="info"><h3>100% Schweizer Honig</h3>
        <div class="field"><span>Mindestens haltbar bis:</span><i></i></div>
        <div class="field"><span>Lot Nr.:</span><i></i></div>
        <div class="weight">Netto <b>500 g</b></div>
        <div class="address">Familie Dorbach, Birkeneck, CH-9573 Holtikon</div></div>
    </article>

    <article class="label wald-dunkel" style="top:204px">
      <div class="variety"><h2>Waldhonig</h2><div class="region">Natürliches aus dem Thurgau</div><div class="rule"></div>
        <p class="story">Honig ist ein Naturprodukt und sein Geschmack variiert je nach Nektarangebot von Jahr zu Jahr. Wir tragen Sorge zu unseren Bienen und bieten ihnen auf unserer Wiesenblumenwiese und den Obstanlagen vom Frühling bis in den Herbst ein vielfältiges Nahrungsangebot. Die reiche Vielfalt an Wiesenblumen gibt unserem Honig seinen milden und im Gaumen gehaltvollen Geschmack.</p></div>
      <div class="comb" role="img" aria-label="Wabenmuster"></div>
      <div class="house" role="img" aria-label="Stilisiertes Riegelhaus mit Biene"></div>
      <div class="brand">Birkeneck</div>
      <div class="info"><h3>100% Schweizer Honig</h3>
        <div class="field"><span>Mindestens haltbar bis:</span><i></i></div>
        <div class="field"><span>Lot Nr.:</span><i></i></div>
        <div class="weight">Netto <b>500 g</b></div>
        <div class="address">Familie Dorbach, Birkeneck, CH-9573 Holtikon</div></div>
    </article>

    <article class="label wald-gruen" style="top:295px">
      <div class="variety"><h2>Waldhonig</h2><div class="region">Natürliches aus dem Thurgau</div><div class="rule"></div>
        <p class="story">Honig ist ein Naturprodukt und sein Geschmack variiert je nach Nektarangebot von Jahr zu Jahr. Wir tragen Sorge zu unseren Bienen und bieten ihnen auf unserer Wiesenblumenwiese und den Obstanlagen vom Frühling bis in den Herbst ein vielfältiges Nahrungsangebot. Die reiche Vielfalt an Wiesenblumen gibt unserem Honig seinen milden und im Gaumen gehaltvollen Geschmack.</p></div>
      <div class="comb" role="img" aria-label="Wabenmuster"></div>
      <div class="house" role="img" aria-label="Stilisiertes Riegelhaus mit Biene"></div>
      <div class="brand">Birkeneck</div>
      <div class="info"><h3>100% Schweizer Honig</h3>
        <div class="field"><span>Mindestens haltbar bis:</span><i></i></div>
        <div class="field"><span>Lot Nr.:</span><i></i></div>
        <div class="weight">Netto <b>500 g</b></div>
        <div class="address">Familie Dorbach, Birkeneck, CH-9573 Holtikon</div></div>
    </article>

    <article class="label lavendel" style="top:398px">
      <div class="variety"><h2>Lavendelhonig</h2><div class="region">Natürliches aus dem Thurgau</div><div class="rule"></div>
        <p class="story">Diesen Lavendelhonig haben unsere Bienen auf unserem eigenen Lavendelfeld gesammelt. Wir ernten ihn nur einmal im Jahr, wenn der Lavendel in Vollblüte steht. Dieser rare Honig zeichnet sich durch seinen typischen Lavendelgeschmack aus.</p></div>
      <div class="comb" role="img" aria-label="Wabenmuster"></div>
      <div class="house" role="img" aria-label="Stilisiertes Riegelhaus mit Biene"></div>
      <div class="brand">Birkeneck</div>
      <div class="info"><h3>100% Schweizer Honig</h3>
        <div class="field"><span>Mindestens haltbar bis:</span><i></i></div>
        <div class="field"><span>Lot Nr.:</span><i></i></div>
        <div class="weight">Netto <b>500 g</b></div>
        <div class="address">Familie Dorbach, Birkeneck, CH-9573 Holtikon</div></div>
    </article>
  </section>

  <!-- Pollen 100 g -->
  <section class="column col-pollen">
    <article class="label pollen pollen-1007" style="top:37px">
      <div class="variety"><h2>Blütenpollen</h2><div class="region">Natürliches aus dem Thurgau</div><div class="rule"></div>
        <p class="story">Den Blütenpollen sammeln unsere Bienen mehrheitlich direkt von unserer Wiesenblumenwiese oder dem Lavendelfeld. Wir verarbeiten den Blütenpollen täglich frisch. Er ist ein hochwertiges Naturprodukt mit vielen lebenswichtigen Substanzen und Wirkstoffen: Vitamine, Mineralien, Proteine, Kohlenhydrate, Fette, Enzyme, essentielle Aminosäuren. Ein bestimmtes Enzym sorgt auch dafür, dass die Blütenpollen haltbar werden und vor Keimen und Gärprozessen geschützt sind. Wir bieten unseren Pollen in getrockneter Form an.</p></div>
      <div class="comb" role="img" aria-label="Wabenmuster"></div>
      <div class="house" role="img" aria-label="Stilisiertes Riegelhaus mit Biene"></div>
      <div class="brand">Birkeneck</div>
      <div class="info"><h3>100% Schweizer Honig</h3>
        <div class="field"><span>Mindestens haltbar bis:</span><i></i></div>
        <div class="field"><span>Lot Nr.:</span><i></i></div>
        <div class="weight">Netto <b>100 g</b></div>
        <div class="address">Familie Dorbach, Birkeneck, CH-9573 Holtikon</div></div>
    </article>

    <article class="label pollen pollen-1033" style="top:128px">
      <div class="variety"><h2>Blütenpollen</h2><div class="region">Natürliches aus dem Thurgau</div><div class="rule"></div>
        <p class="story">Den Blütenpollen sammeln unsere Bienen mehrheitlich direkt von unserer Wiesenblumenwiese oder dem Lavendelfeld. Wir verarbeiten den Blütenpollen täglich frisch. Er ist ein hochwertiges Naturprodukt mit vielen lebenswichtigen Substanzen und Wirkstoffen: Vitamine, Mineralien, Proteine, Kohlenhydrate, Fette, Enzyme, essentielle Aminosäuren. Ein bestimmtes Enzym sorgt auch dafür, dass die Blütenpollen haltbar werden und vor Keimen und Gärprozessen geschützt sind. Wir bieten unseren Pollen in getrockneter Form an.</p></div>
      <div class="comb" role="img" aria-label="Wabenmuster"></div>
      <div class="house" role="img" aria-label="Stilisiertes Riegelhaus mit Biene"></div>
      <div class="brand">Birkeneck</div>
      <div class="info"><h3>100% Schweizer Honig</h3>
        <div class="field"><span>Mindestens haltbar bis:</span><i></i></div>
        <div class="field"><span>Lot Nr.:</span><i></i></div>
        <div class="weight">Netto <b>100 g</b></div>
        <div class="address">Familie Dorbach, Birkeneck, CH-9573 Holtikon</div></div>
    </article>

    <article class="label pollen pollen-2003" style="top:218px">
      <div class="variety"><h2>Blütenpollen</h2><div class="region">Natürliches aus dem Thurgau</div><div class="rule"></div>
        <p class="story">Den Blütenpollen sammeln unsere Bienen mehrheitlich direkt von unserer Wiesenblumenwiese oder dem Lavendelfeld. Wir verarbeiten den Blütenpollen täglich frisch. Er ist ein hochwertiges Naturprodukt mit vielen lebenswichtigen Substanzen und Wirkstoffen: Vitamine, Mineralien, Proteine, Kohlenhydrate, Fette, Enzyme, essentielle Aminosäuren. Ein bestimmtes Enzym sorgt auch dafür, dass die Blütenpollen haltbar werden und vor Keimen und Gärprozessen geschützt sind. Wir bieten unseren Pollen in getrockneter Form an.</p></div>
      <div class="comb" role="img" aria-label="Wabenmuster"></div>
      <div class="house" role="img" aria-label="Stilisiertes Riegelhaus mit Biene"></div>
      <div class="brand">Birkeneck</div>
      <div class="info"><h3>100% Schweizer Honig</h3>
        <div class="field"><span>Mindestens haltbar bis:</span><i></i></div>
        <div class="field"><span>Lot Nr.:</span><i></i></div>
        <div class="weight">Netto <b>100 g</b></div>
        <div class="address">Familie Dorbach, Birkeneck, CH-9573 Holtikon</div></div>
    </article>
  </section>

  <p class="ral" style="top:81px;margin:0">RAL 1007</p>
  <p class="ral" style="top:172px;margin:0">RAL 1033</p>
  <p class="ral" style="top:261px;margin:0;left:1166px">RAL 2003</p>

</main>
</body>
</html>
```